Corlith Australia Pty Ltd

I require professional business cards with our company logo. We would like something that looks sharp and unique. I have attached the logo for our business, which is an industrial electrical contracting company. But this does not need to be shown on the cards.

Requirements
Must have
• The design must be double sided and needs to have one side with our logo only and the other side with our details.
Should not have
• We do not want any lightening bolts on the designs as this is very common.

```html
<!DOCTYPE html>
<html lang="en">
<head>
<meta charset="utf-8">
<title>Corlith Australia Pty Ltd – Business Cards</title>
<link rel="stylesheet" href="https://fonts.googleapis.com/css2?family=Arimo:wght@400;700&display=swap">
<style>
  :root {
    --backdrop: #3a3b3a;
    --card: #ffffff;
    --ink: #1d1d1d;
    --gold: #b8943f;
    --watermark: #eeeeee;
  }
  * { box-sizing: border-box; margin: 0; padding: 0; }
  html, body { width: 1200px; height: 800px; overflow: hidden; }
  body {
    background: var(--backdrop);
    font-family: "Arimo", Arial, sans-serif;
    color: var(--ink);
    position: relative;
  }
  .card {
    position: absolute;
    top: 242px;
    width: 540px;
    height: 315px;
    background: var(--card);
    overflow: hidden;
    box-shadow: 0 10px 30px rgba(0,0,0,0.35);
  }
  .card--front { left: 40px; }
  .card--back { left: 620px; }

  /* Front: brand lockup */
  .brand {
    position: absolute;
    left: 50%; top: 50%;
    transform: translate(-50%, -50%);
    display: flex;
    align-items: center;
    gap: 14px;
    white-space: nowrap;
  }
  .brand__dot {
    width: 46px; height: 46px;
    border-radius: 50%;
    background: var(--gold);
    flex: none;
  }
  .brand__name {
    font-weight: 700;
    font-size: 24px;
    color: var(--gold);
    letter-spacing: 0.5px;
  }

  /* Back: details */
  .card__watermark {
    position: absolute;
    left: 290px; top: 80px;
    width: 270px; height: 270px;
    border-radius: 50%;
    border: 24px solid var(--watermark);
  }
  .card__mark {
    position: absolute;
    left: 40px; top: 30px;
    width: 52px; height: 52px;
    border-radius: 50%;
    background: var(--gold);
  }
  .details {
    position: absolute;
    left: 40px; top: 128px;
  }
  .details__company { font-weight: 700; font-size: 19px; line-height: 1.15; }
  .details__address { font-size: 14px; margin-bottom: 12px; }
  .contact { list-style: none; font-size: 13.5px; line-height: 1.35; }
  .contact li { display: flex; align-items: center; gap: 8px; }
  .contact svg { width: 11px; height: 11px; fill: var(--ink); flex: none; }
  .person {
    position: absolute;
    right: 40px; top: 186px;
    text-align: right;
  }
  .person__name { font-weight: 700; font-size: 17px; }
  .person__role { font-weight: 700; font-size: 16px; color: var(--gold); }
</style>
</head>
<body>
  <section class="card card--front" aria-label="Card front">
    <div class="brand">
      <span class="brand__dot"></span>
      <span class="brand__name">Corlith Australia Pty Ltd</span>
    </div>
  </section>

  <section class="card card--back" aria-label="Card back">
    <div class="card__watermark"></div>
    <div class="card__mark"></div>
    <div class="details">
      <p class="details__company">Corlith Australia Pty Ltd.</p>
      <p class="details__address">PO Box 318, Camden Hills NSW 2590</p>
      <ul class="contact">
        <li>
          <svg viewBox="0 0 12 12" aria-hidden="true"><path d="M3 1l2 2.5-1.2 1.2a7 7 0 0 0 3.5 3.5L8.5 7 11 9l-1.2 2C5.5 11 1 6.5 1 2.2z"/></svg>
          02 5550 1827
        </li>
        <li>
          <svg viewBox="0 0 12 12" aria-hidden="true"><path d="M3.5 0h5a1 1 0 0 1 1 1v10a1 1 0 0 1-1 1h-5a1 1 0 0 1-1-1V1a1 1 0 0 1 1-1zm.5 1.5v7.5h4V1.5z"/></svg>
          0400 555 912
        </li>
        <li>
          <svg viewBox="0 0 12 12" aria-hidden="true"><path d="M0 2h12v8H0zm1 1v.4l5 3.2 5-3.2V3z"/></svg>
          rowan@corlithaustralia.com.au
        </li>
        <li>
          <svg viewBox="0 0 12 12" aria-hidden="true"><path d="M6 0a6 6 0 1 0 0 12A6 6 0 0 0 6 0zm0 1.2c.8.9 1.3 2.2 1.4 4.2H4.6C4.7 3.4 5.2 2.1 6 1.2zM1.3 6.6h2.2c.1 1.6.5 3 1.1 4A4.8 4.8 0 0 1 1.3 6.6zm0-1.2a4.8 4.8 0 0 1 3.3-4c-.6 1-1 2.4-1.1 4zm3.3 1.2h2.8c-.1 1.9-.6 3.2-1.4 4.2-.8-1-1.3-2.3-1.4-4.2zm3.9 0h2.2a4.8 4.8 0 0 1-3.3 4c.6-1 1-2.4 1.1-4zm0-1.2c-.1-1.6-.5-3-1.1-4a4.8 4.8 0 0 1 3.3 4z"/></svg>
          www.corlithaustralia.com.au
        </li>
      </ul>
    </div>
    <div class="person">
      <p class="person__name">Rowan Pellow</p>
      <p class="person__role">Director</p>
    </div>
  </section>
</body>
</html>
```